Tuition Center Website

We need a new web site for a tutoring company based in sydney.

We only teach senior highschool students and pride ourselves on building the students abilities to think their way through life.

I would like a bright and vibrant website that looks professional and modern.
It needs to look simple and neat but also have the functionality we need.
Images and flash would be good.

Please keep in mind that the site must be appealing to a younger audience.

We need a multipage website with the following navigation bars:

1.Home (As logo not "home" button)
I would like a news box/ticker somewhere that can stream our chatterbook and peeplr feeds and also any news updates we want to put up.
Subscribe to newsletter button.

2. About us.
This needs to be a pull down into:
-What we do
-Why we do it
-How we do it

3. Courses
Pulldown into:
-Maths
-English
-Science
(we may need to attach extra pages behind these e.g. Courses/Science/Physics or Courses/Science/Chemistry and possibly add a link to a new formvik form)

4. Inspired
This page is like a blog page where we can upload videos, links to articles that we find to be inspiring and hopefully will inspire others.

5. Inspire
This is a recruitment page. Only content here.

6. Contact us.
Trovix map widget and a 'contact us' form

* Our branding requires green close to #12FF3D

***Please have a look at the current website.
@ www.velmoralearning.com.au

Thanks everybody hope the revision of my brief is better and more informative than my last one
Updates

Target Market(s)

senior highschool students aged 15-19, parents ( to a lesser degree)

Industry/Entity Type

It Company

Requirements
Must have
• Ability to change content on pages.

The green doesn't have to be everywhere, but it must be obvious that it is our colour.

Nice to have
• Sites with a nicer mix of images and flash will be given more consideration. But then again, if you amaze us, you amaze us and we will go with your design.
Should not have
• Should stay away from ocre, brown colours and serif fonts.

```html
<!DOCTYPE html>
<html lang="en">
<head>
<meta charset="utf-8">
<title>Velmora Learning – Home</title>
<link href="https://fonts.googleapis.com/css2?family=Open+Sans:wght@400;600;700&family=Kalam:wght@400;700&display=swap" rel="stylesheet">
<style>
:root{
  --green:#86d900;
  --green-bright:#8fe000;
  --green-dark:#5fa800;
  --ink:#111;
  --text:#333;
  --muted:#777;
  --line:#cfcfcf;
  --panel:#f1f1f1;
  --link:#2aa3d6;
}
*{box-sizing:border-box;margin:0;padding:0}
html,body{width:782px;height:1200px;overflow:hidden;background:#fff}
body{font-family:"Open Sans",Arial,sans-serif;color:var(--text)}
.page{position:relative;width:782px;height:1200px;overflow:hidden}
.abs{position:absolute}

/* header */
.brand{left:84px;top:8px;width:120px}
.brand-mark{width:52px;height:46px;background:var(--green-bright);margin-left:6px}
.brand-name{font-size:14px;font-weight:700;color:var(--ink);line-height:15px;margin-top:4px}
.nav{left:302px;top:29px;width:394px;height:31px;background:#1c1c1c;border-radius:3px;display:flex;align-items:center;justify-content:space-around;padding:0 8px}
.nav a{color:#fff;font-size:10px;text-decoration:none;padding:4px 7px}
.nav a.active{background:var(--green);border-radius:2px;font-weight:600}

/* hero */
.hero{left:79px;top:93px;width:624px;height:268px;background:var(--green-bright);overflow:hidden}
.hero-photo{position:absolute;right:0;top:0;width:300px;height:268px;background:linear-gradient(90deg,var(--green-bright) 0%,#c9b59e 35%,#9a7c74 70%,#6a4a55 100%)}
.hero h1{position:absolute;left:11px;top:52px;color:#fff;font-size:24px;font-weight:700;letter-spacing:.3px;text-shadow:0 1px 2px rgba(0,0,0,.25)}
.hero h2{position:absolute;left:11px;top:80px;color:#fff;font-size:15px;font-weight:600;text-shadow:0 1px 2px rgba(0,0,0,.25)}
.hero p{position:absolute;left:11px;top:110px;width:260px;font-size:8.5px;line-height:15px;color:#111}
.btn-dark{background:#151515;color:#fff;font-weight:700;display:inline-block;border-radius:2px}
.hero .btn-dark{position:absolute;left:12px;top:166px;width:120px;height:30px;line-height:30px;text-align:center;font-size:11px}
.dots{position:absolute;left:15px;top:230px;display:flex;gap:7px}
.dots span{width:7px;height:7px;border-radius:50%;background:#111}
.dots span.on{background:#fff}

/* intro */
.intro{left:87px;top:395px;width:380px}
.intro h3{font-size:17px;font-weight:700;color:var(--ink);margin-bottom:12px}
.intro p{font-size:10px;line-height:17.5px;color:#111}
.intro-art{left:504px;top:372px;width:184px;height:148px;background:radial-gradient(circle at 50% 50%,#eef8df 0%,#fff 75%);border-radius:6px}

/* beliefs */
.beliefs{left:79px;top:536px;width:407px;height:149px;background:var(--panel);border:1px solid #d3d3d3}
.belief-col{position:absolute;top:20px;width:190px}
.belief-col h4{font-family:"Kalam",cursive;font-weight:700;font-size:17px;color:var(--green-dark);display:flex;align-items:center;gap:8px;margin-left:7px}
.belief-col ul{list-style:none;margin:20px 0 0 32px}
.belief-col li{font-size:8.5px;color:#222;display:flex;gap:8px;margin-bottom:7px;line-height:12px}
.belief-col li svg{flex:none;margin-top:1px}

/* news */
.news{left:512px;top:536px;width:190px;height:149px;border-bottom:1px dashed #aaa}
.news-title{display:flex;align-items:center;gap:8px;font-size:13px;color:var(--ink)}
.news-title b{font-weight:400;color:var(--green-dark)}
.news-item{position:relative;margin:10px 0 0 10px;padding-left:12px;width:158px}
.news-item::before{content:"{";position:absolute;left:-2px;top:-3px;font-size:30px;color:var(--green-dark);font-weight:300;line-height:34px}
.news-item p{font-size:7px;line-height:9.5px;color:#555}
.news-item time{display:block;text-align:right;font-size:7px;font-weight:700;color:#111;margin-top:3px}
.news-more{margin:6px 0 0 28px;font-size:7.5px;font-weight:700;color:#111}
.news-track{position:absolute;right:0;top:16px;height:128px;border-left:1px dotted #555}
.news-thumb{position:absolute;right:-2px;top:44px;width:4px;height:16px;background:var(--green-dark);border-radius:2px}

/* tweet bar */
.tweet{left:78px;top:709px;width:625px;height:32px;background:#ececec;display:flex;align-items:center;padding-left:42px;font-size:8px;color:#333;gap:6px}
.tweet .handle,.tweet .url{color:var(--link)}
.tweet .date{margin-left:40px;font-size:7px;color:#666}

/* welcome */
.welcome{left:79px;top:766px;width:390px}
.welcome h3{font-size:13px;font-weight:400;color:#222;padding-bottom:8px;border-bottom:1px dashed #bbb}
.welcome p{font-size:7.8px;line-height:12px;color:#777;margin-top:12px}
.welcome .btn-dark{margin-top:14px;width:86px;height:24px;line-height:24px;text-align:center;font-size:11px;font-weight:600}

.trial{left:507px;top:769px;width:195px;height:157px;background:linear-gradient(#7fd000,#62b000);border:2px solid #b9d98f;border-radius:2px;color:#fff}
.trial h3{font-size:20px;font-weight:400;color:#111;text-align:center;margin-top:14px}
.trial-icon{position:absolute;left:12px;top:62px;width:30px;height:30px;border:1.5px solid #dff3c2;border-radius:3px}
.trial p{position:absolute;left:54px;top:56px;width:136px;font-size:9px;line-height:13px}
.trial .btn-dark{position:absolute;left:50px;top:118px;width:101px;height:23px;line-height:23px;text-align:center;font-size:10px;font-weight:700;border-radius:0}

/* footer */
.footer{left:79px;top:948px;width:624px;height:196px;background:linear-gradient(#f2f2f2,#fff 60%);border-top:1px solid #c8e29f}
.fcol{position:absolute;top:20px;width:178px}
.fcol h5{font-size:11px;font-weight:400;color:#111;text-align:center;padding-bottom:10px;border-bottom:1px dashed #aaa}
.fb-box{margin-top:17px;height:130px;border:1px solid #cfcfcf;background:#fff;position:relative}
.fb-head{display:flex;gap:8px;padding:6px;border-bottom:1px solid #ddd}
.fb-sq{width:26px;height:26px;background:var(--green-bright);flex:none}
.fb-name{font-size:8.5px;color:#3b5a9a}
.fb-like{font-size:6.5px;border:1px solid #bbb;padding:1px 4px;margin-top:2px;display:inline-block;color:#444}
.fb-post{display:flex;gap:8px;padding:6px}
.fb-post p{font-size:7px;line-height:11px;color:#333}
.fb-scroll{position:absolute;right:1px;top:42px;width:8px;height:86px;background:#eee;border-left:1px solid #ddd}
.nl p{font-size:7.5px;line-height:12px;color:#333;margin-top:14px}
.nl label{display:block;font-size:7.5px;margin-top:10px;color:#333}
.nl .field{width:143px;height:20px;border:1px solid #bbb;margin-top:4px;background:#fff}
.nl .sub{display:inline-block;margin-top:10px;background:#111;color:#fff;font-size:7.5px;padding:3px 8px}
.social{display:flex;gap:11px;margin-top:14px;padding-left:2px}
.social span{width:17px;height:17px;border-radius:50%;background:#a5a5a5}
.contact p{font-size:7.5px;line-height:13px;color:#222;margin-top:12px}

.copy{left:0;top:1168px;width:782px;text-align:center;font-size:8px;color:#666}
.copy a{color:var(--green-dark);text-decoration:none}
</style>
</head>
<body>
<div class="page">

  <div class="abs brand">
    <div class="brand-mark"></div>
    <div class="brand-name">velmora<br>learning</div>
  </div>

  <nav class="abs nav">
    <a class="active">Home</a><a>About Us</a><a>Courses</a><a>Inspired</a><a>Inspire</a><a>Contact Us</a>
  </nav>

  <section class="abs hero">
    <div class="hero-photo" role="img" aria-label="Photo of a smiling student holding a pencil and a book"></div>
    <h1>I AM VELMORA</h1>
    <h2>real HSC coaching &amp; mentoring.</h2>
    <p>The HSC help you need, in the years you need it. We offer small classes, individualised attention and genuine care for each student. It's different - in a good way.</p>
    <span class="btn-dark">ENQUIRE NOW</span>
    <div class="dots"><span></span><span class="on"></span><span></span></div>
  </section>

  <section class="abs intro">
    <h3>Real HSC coaching &amp; mentoring.</h3>
    <p>The HSC help you need, in the years you need it. We offer small classes, individualised attention and genuine care for each student. It's different - in a good way. Feel free to find out more about us, and let us know if there's any way we can help you on your journey.</p>
  </section>
  <div class="abs intro-art" role="img" aria-label="Green doodle illustration of study sketches, pencils and HSC scribbles"></div>

  <section class="abs beliefs">
    <div class="belief-col" style="left:0">
      <h4><svg width="32" height="28" viewBox="0 0 32 28"><rect x="4" y="6" width="26" height="16" fill="none" stroke="#555" stroke-width="2"/><rect x="14" y="22" width="6" height="4" fill="#555"/><circle cx="8" cy="8" r="5" fill="#666"/></svg>We Don't Believe In:</h4>
      <ul>
        <li><svg width="12" height="10" viewBox="0 0 12 10"><path d="M1 3v6h8V6" fill="none" stroke="#5fa800" stroke-width="1.5"/><path d="M4 6l6-5M7 1h3v3" fill="none" stroke="#5fa800" stroke-width="1.5"/></svg>Massive classes;</li>
        <li><svg width="12" height="10" viewBox="0 0 12 10"><path d="M1 3v6h8V6" fill="none" stroke="#5fa800" stroke-width="1.5"/><path d="M4 6l6-5M7 1h3v3" fill="none" stroke="#5fa800" stroke-width="1.5"/></svg>Spoon-feeding answers;</li>
        <li><svg width="12" height="10" viewBox="0 0 12 10"><path d="M1 3v6h8V6" fill="none" stroke="#5fa800" stroke-width="1.5"/><path d="M4 6l6-5M7 1h3v3" fill="none" stroke="#5fa800" stroke-width="1.5"/></svg>One-size-fits-all teaching.</li>
      </ul>
    </div>
    <div class="belief-col" style="left:205px">
      <h4><svg width="32" height="28" viewBox="0 0 32 28"><rect x="2" y="4" width="26" height="18" fill="none" stroke="#555" stroke-width="2"/><path d="M6 10h12M6 14h12M6 18h8" stroke="#555" stroke-width="2"/><circle cx="25" cy="22" r="4" fill="#666"/></svg>We Do Believe In:</h4>
      <ul>
        <li><svg width="12" height="10" viewBox="0 0 12 10"><path d="M1 3v6h8V6" fill="none" stroke="#5fa800" stroke-width="1.5"/><path d="M4 6l6-5M7 1h3v3" fill="none" stroke="#5fa800" stroke-width="1.5"/></svg>Small classes tailored to you;</li>
        <li><svg width="12" height="10" viewBox="0 0 12 10"><path d="M1 3v6h8V6" fill="none" stroke="#5fa800" stroke-width="1.5"/><path d="M4 6l6-5M7 1h3v3" fill="none" stroke="#5fa800" stroke-width="1.5"/></svg>Helping you think for yourself;</li>
        <li><svg width="12" height="10" viewBox="0 0 12 10"><path d="M1 3v6h8V6" fill="none" stroke="#5fa800" stroke-width="1.5"/><path d="M4 6l6-5M7 1h3v3" fill="none" stroke="#5fa800" stroke-width="1.5"/></svg>Genuinely caring about who you<br>are as an individual.</li>
      </ul>
    </div>
  </section>

  <aside class="abs news">
    <div class="news-title"><svg width="30" height="24" viewBox="0 0 30 24"><rect x="3" y="4" width="24" height="17" fill="#eee" stroke="#777" transform="rotate(-10 15 12)"/><path d="M8 10h14M8 13h14M8 16h10" stroke="#999" transform="rotate(-10 15 12)"/></svg>News <b>Updates</b></div>
    <div class="news-item"><p>Lorem Ipsum is simply dummy text of the printing and typesetting industry. Lorem Ipsum has been the industry's</p><time>25-Feb-2013</time></div>
    <div class="news-item"><p>Lorem Ipsum is simply dummy text of the printing and typesetting industry. Lorem Ipsum has been the industry's</p><time>25-Feb-2013</time></div>
    <div class="news-more">→ Read More</div>
    <div class="news-track"></div><div class="news-thumb"></div>
  </aside>

  <div class="abs tweet">
    <svg width="18" height="18" viewBox="0 0 18 18"><circle cx="9" cy="9" r="8" fill="#2aa3d6"/></svg>
    <span style="color:#999">|</span>
    <span class="handle">@1345Velmora</span>
    <span>This is a tweet from Fresh Studio , you can link your peeplr from here</span>
    <span class="url">vlm.to/VLtCLx</span>
    <span class="date">30 Dec</span>
  </div>

  <section class="abs welcome">
    <h3>Welcome to Velmora Learning</h3>
    <p>Lorem Ipsum is simply dummy text of the printing and typesetting industry. Lorem Ipsum has been the industry's standard dummy text ever since the 1500s, when an unknown printer took a galley of type and scrambled it to make a type specimen book.</p>
    <p>Lorem Ipsum is simply dummy text of the printing and typesetting industry. Lorem Ipsum has been the industry's standard dummy text ever since the 1500s, when an unknown printer took a galley of type and scrambled it to make a type specimen book.</p>
    <span class="btn-dark">Read More</span>
  </section>

  <aside class="abs trial">
    <h3>Free Trial Lesson</h3>
    <div class="trial-icon" role="img" aria-label="Small chalkboard doodle"></div>
    <p>Because we believe you shouldn't have to sign up until you see what it's actually like. Call or email us now!</p>
    <span class="btn-dark">Send an Enquiry</span>
  </aside>

  <footer class="abs footer">
    <div class="fcol" style="left:7px">
      <h5>Chatterbook News</h5>
      <div class="fb-box">
        <div class="fb-head"><div class="fb-sq"></div><div><div class="fb-name">Velmora</div><span class="fb-like">Like</span></div></div>
        <div class="fb-post"><div class="fb-sq"></div><div><div class="fb-name">Velmora</div><p>Get creative and use your braaaaaaaains.</p><p style="margin-top:8px">Design a tee perfectly suited to anyone who digs the undead.</p></div></div>
        <div class="fb-scroll"></div>
      </div>
    </div>
    <div class="fcol nl" style="left:216px">
      <h5>Newsletters</h5>
      <p>Get , our monthly newsletter, delivered to your inbox each month</p>
      <label>Your Name:</label><div class="field"></div>
      <label>Your E-mail:</label><div class="field"></div>
      <span class="sub">Subscribe</span>
    </div>
    <div class="fcol contact" style="left:417px;width:196px">
      <h5>Contact Us</h5>
      <div class="social"><span></span><span></span><span></span><span></span><span></span><span></span><span></span></div>
      <p>Get in touch with us to know how we can help you better</p>
      <p>Street: 48 Harlow St Ashgrove NSW 2199<br>Phone: (02) 5550 1457<br>Email: learn@velmoralearning.com.au</p>
    </div>
  </footer>

  <div class="abs copy"><a>Privacy Policy</a> &nbsp;|&nbsp; Copyright © 2013 - 2013 Velmora Learning</div>
</div>
</body>
</html>
```